Vendrick Legal PLLC updated letterhead for solo law practice - legal/professional services

I need a new letterhead design on a word document for my solo law practice. I have attached my current letterhead. Here is my company info:

Dorian Vendrick
Vendrick Legal PLLC
2718 Brambleton, Suite 430
Dallas, Texas 75291
Phone: 214 555 0187
Email: dorian@vendrick-legal.example
Website: www.vendrick-legal.example

Preferably I'd like the logo on top followed by my name and email (in the header)

At the bottom (footer) i'd like the rest of the information.

I am fine using a color for the line in between "Vendrick" and "Legal" in the "Vendrick Legal" logo. Or a different font.

Industry/Entity Type

Legal

Font styles to use
Serif

Colors

Designer to choose only greyscale colors for use in the design.

Requirements
Must have
• The "Vendrick Legal" logo with the line in between "Vendrick" and "Legal" but I am open to ideas on structure and color schemes.
Nice to have
• Logo on top with new color scheme, along with my name and email.
• Address, phone number, web address on bottom.

```html
<!DOCTYPE html>
<html lang="en">
<head>
<meta charset="utf-8">
<title>Vendrick Legal PLLC — Letterhead</title>
<link href="https://fonts.googleapis.com/css2?family=Tinos:wght@400;700&display=swap" rel="stylesheet">
<style>
  :root {
    --backdrop: #dcdcdc;
    --paper: #ececec;
    --band: #555555;
    --accent: #6e6e6e;
    --ink: #141414;
    --text: #222222;
    --white: #ffffff;
  }
  * { margin: 0; padding: 0; box-sizing: border-box; }
  html, body {
    width: 1200px;
    height: 1017px;
    overflow: hidden;
    background: var(--backdrop);
  }
  .letterhead {
    position: absolute;
    left: 230px;
    top: 27px;
    width: 818px;
    height: 1063px;
    background: var(--paper);
    transform: scale(0.905);
    transform-origin: top left;
    font-family: "Tinos", "Times New Roman", serif;
    color: var(--text);
  }
  .header-band, .footer-band {
    position: absolute;
    left: 0;
    width: 818px;
    display: block;
  }
  .header-band { top: 0; height: 45px; }
  .footer-band { bottom: 0; height: 45px; }

  .wordmark {
    position: absolute;
    left: 29px;
    top: 62px;
    display: flex;
    align-items: center;
    font-size: 34px;
    line-height: 1;
    color: var(--ink);
  }
  .wordmark-divider {
    display: inline-block;
    width: 2px;
    height: 48px;
    background: var(--accent);
    margin: 0 9px;
  }

  .sender {
    position: absolute;
    right: 31px;
    top: 67px;
    text-align: right;
  }
  .sender-name {
    font-weight: 700;
    font-size: 13px;
    color: var(--ink);
  }
  .sender-email {
    margin-top: 7px;
    font-size: 12px;
    display: flex;
    align-items: center;
    justify-content: flex-end;
    gap: 10px;
  }

  .contact-line {
    position: absolute;
    left: 29px;
    top: 996px;
    display: flex;
    align-items: center;
    font-size: 12px;
    gap: 5px;
  }
  .contact-line .spacer { width: 3px; }

  .address {
    position: absolute;
    left: 29px;
    top: 1033px;
    display: flex;
    align-items: center;
    gap: 10px;
    font-size: 12px;
    color: var(--white);
  }
  .icon { display: block; }
</style>
</head>
<body>
  <article class="letterhead">
    <svg class="header-band" viewBox="0 0 818 45" aria-hidden="true">
      <path d="M0 0 H818 V41 H402 C372 41 362 19 334 15 H0 Z" fill="var(--band)"/>
      <path d="M0 21 H334 C344 21 352 25 360 30 H0 Z" fill="var(--ink)"/>
    </svg>

    <header>
      <div class="wordmark">
        <span class="wordmark-first">VENDRICK</span>
        <span class="wordmark-divider"></span>
        <span class="wordmark-second">LEGAL</span>
      </div>
      <div class="sender">
        <div class="sender-name">Dorian Vendrick</div>
        <div class="sender-email">
          <span>dorian@vendrick-legal.example</span>
          <svg class="icon" width="8" height="6" viewBox="0 0 8 6" aria-hidden="true">
            <rect width="8" height="6" fill="var(--band)"/>
            <path d="M0.8 1 L4 3.4 L7.2 1" fill="none" stroke="var(--white)" stroke-width="0.8"/>
          </svg>
        </div>
      </div>
    </header>

    <footer>
      <div class="contact-line">
        <svg class="icon" width="10" height="10" viewBox="0 0 10 10" aria-hidden="true">
          <path d="M2 1 L3.6 1 L4.2 3 L3.2 3.8 C3.8 5 4.9 6.1 6.2 6.8 L7 5.8 L9 6.4 L9 8 C9 8.6 8.6 9 8 9 C4.5 9 1 5.5 1 2 C1 1.4 1.4 1 2 1 Z" fill="var(--band)"/>
        </svg>
        <span>214 555 0187</span>
        <span class="spacer"></span>
        <svg class="icon" width="10" height="10" viewBox="0 0 10 10" aria-hidden="true">
          <circle cx="5" cy="5" r="4.5" fill="var(--band)"/>
          <path d="M0.5 5 H9.5 M5 0.5 C3 3 3 7 5 9.5 M5 0.5 C7 3 7 7 5 9.5" fill="none" stroke="var(--paper)" stroke-width="0.7"/>
        </svg>
        <span>www.vendrick-legal.example</span>
      </div>

      <svg class="footer-band" viewBox="0 0 818 45" aria-hidden="true">
        <path d="M0 3 H410 C440 3 452 18 482 28 H818 V45 H0 Z" fill="var(--band)"/>
        <path d="M458 14 H818 V23 H478 C470 21 464 18 458 14 Z" fill="var(--ink)"/>
      </svg>

      <div class="address">
        <svg class="icon" width="16" height="16" viewBox="0 0 16 16" aria-hidden="true">
          <circle cx="8" cy="8" r="7.2" fill="none" stroke="var(--white)" stroke-width="1"/>
          <path d="M8 3.6 C6.2 3.6 5 4.9 5 6.5 C5 8.6 8 12 8 12 C8 12 11 8.6 11 6.5 C11 4.9 9.8 3.6 8 3.6 Z" fill="var(--white)"/>
          <circle cx="8" cy="6.5" r="1.1" fill="var(--band)"/>
        </svg>
        <span>Vendrick Legal PLLC 2718 Brambleton, Suite 430 Dallas, Texas 75291</span>
      </div>
    </footer>
  </article>
</body>
</html>
```